Announcement for a New Trauma Therapy Group - Rack Card

I need a two-sided "rack" card that is 4x9 announcing a Women's Trauma and Loss Group. I am a licensed therapist and will be starting this support group for women who have experienced trauma of all kinds. In addition to groups, I offer individual, couples, and family counseling sessions.

I would like to see designs that are soft tones and use colors like muted blues, greens, and sand tones. The final design should communicate hope and healing as well as have a peaceful feel to it.

I would like a picture of a woman's profile from either the side or from behind her. (possibly a contemplative picture on a beach)

I am attaching a picture of myself to go alongside the bio information as well.

On One Side, I need the description of the group and contact info:

Mending the Weary Spirit
Women's Trauma & Loss Group
Led by Licensed Professional Counselor, Jen Dalby Rusk

10 Week Group
Cost - $35 session
Group size limited to 10 participants

Topics Include:
What is Trauma?
How Trauma Affects Us
Creating a Feeling of Safety
Managing Trauma Triggers
Importance of Self Care
Healthy vs. Unhealthy Coping
Guilt, Shame, and Blame
Victim vs. Victimized
Grieving through Loss
Anger and Forgiveness
Imagining a Better Future

For More Information, Contact:
Jen Dalby Rusk, LPC, LMFT
(555) 614-3920
jen@brightmeadowcare.example

On Side Two:

Life hurts and does not seem fair. So what do you do when you are faced with an event in your life that knocks you off your feet? It seems no one understands what you are feeling and no one knows just what to say. It is tempting to pull away and isolate or put up a mask and pretend everything is OK.

It is my desire you know that you are not alone! There are others who understand the feelings you are going through and offer a safe place for encouraging support. I want to invite you to embark on a courageous journey of healing where you will not only learn how to "survive" after trauma and loss, but instead, learn that you can once again "thrive"!
- Jen Dalby Rusk, LPC, LMFT

Jen Dalby Rusk is a Licensed Professional Counselor and Licensed Marriage and Family Therapist. She is the owner of Quiet Harbor Counseling Services located in Maple Bend, OK.

Jen is a trauma survivor herself and understands firsthand the unique challenges that can arise on the journey to healing.

(Include Jen's picture next to bio)

(Attach logo and business information to this side as well.)

Target Market(s)

Women who have gone through a traumatic experience or loss and are hurting emotionally

Industry/Entity Type

Counsellor

Font styles to use
Serif
Script

Colors
fbe7d2
86cfc6
cfeae6
85abd2
cfdeed

Requirements
Must have
• Jen's picture as well as her logo and contact information must be on the card.
• One side of the card should describe the group with the following description:
• "Mending the Weary Spirit"
• Women's Trauma & Loss Group
• Led by Licensed Professional Counselor, Jen Dalby Rusk
• 10 Week Group
• Cost - $35 session
• Group size limited to 10 participants
• Topics Include:
• What is Trauma?
• How Trauma Affects Us
• Creating a Feeling of Safety
• Managing Trauma Triggers
• Importance of Self Care
• Healthy vs. Unhealthy Coping
• Guilt, Shame, and Blame
• Victim vs. Victimized
• Grieving through Loss
• Anger and Forgiveness
• Imagining a Better Future
• For More Information, Contact:
• Jen Dalby Rusk, LPC, LMFT
• (555) 614-3920
• jen@brightmeadowcare.example
• On the second side, it must have this note from Jen:
• Life hurts and does not seem fair. So what do you do when you are faced with an event in your life that knocks you off your feet? It seems no one understands what you are feeling and no one knows just what to say. It is tempting to pull away and isolate or put up a mask and pretend everything is OK.
• It is my desire you know that you are not alone! There are others who understand the feelings you are going through and offer a safe place for encouraging support. I want to invite you to embark on a courageous journey of healing where you will not only learn how to "survive" after trauma and loss, but instead, learn that you can once again "thrive"!
• - Jen Dalby Rusk, LPC, LMFT
• Jen Dalby Rusk is a Licensed Professional Counselor and Licensed Marriage and Family Therapist. She is the owner of Quiet Harbor Counseling Services located in Maple Bend, OK.
• Jen is a trauma survivor herself and understands firsthand the unique challenges that can arise on the journey to healing. In addition to facilitating groups, Jen also offers individual, marriage, and family counseling.
Nice to have
• soft muted colors that are peaceful. Light blues, greens, sand colors would work well. A picture at the top of the card of either a woman or a woman's profile that is hopeful such as a woman sitting at a beach overlooking the ocean.
Should not have
• No harsh or bright bold colors. This card needs to have a peaceful feeling to it.

```html
<!DOCTYPE html>
<html lang="en">
<head>
<meta charset="utf-8">
<title>Mending the Weary Spirit – Rack Card</title>
<link href="https://fonts.googleapis.com/css2?family=Oswald:wght@300;500;700&family=Lato:wght@400;700;900&family=Josefin+Sans:wght@400;600&family=Varela+Round&display=swap" rel="stylesheet">
<style>
  :root{
    --stage:#727377;
    --paper:#f6f6f6;
    --sage:#9ac9aa;
    --mist-blue:#a7c3d3;
    --forest:#4b7d2f;
    --slate:#818386;
    --ink:#3f4042;
    --body-grey:#6d6f72;
    --white:#ffffff;
  }
  *{margin:0;padding:0;box-sizing:border-box}
  html,body{width:1034px;height:1200px;overflow:hidden;background:var(--stage)}
  .card{position:absolute;top:186px;width:368px;height:829px;background:var(--paper);overflow:hidden;font-family:"Lato",sans-serif}
  .card--front{left:118px}
  .card--back{left:542px}

  /* front */
  .hero-photo{position:absolute;left:0;top:0;width:368px;height:446px;
    background:linear-gradient(180deg,#f4ece1 0%,#efe7dc 45%,#c9c8c2 70%,#8e9192 85%,#b7b4ac 100%)}
  .brand{position:absolute;display:flex;align-items:center;gap:6px;font-family:"Lato",sans-serif;font-weight:700;color:var(--forest)}
  .brand__dot{width:12px;height:12px;border-radius:50%;background:var(--forest);flex:none}
  .brand--front{left:30px;top:70px;font-size:15px;line-height:1.15;width:150px}
  .title{position:absolute;left:200px;top:22px;font-family:"Oswald",sans-serif;font-weight:700;text-transform:uppercase;line-height:.98;letter-spacing:-.5px}
  .title span{display:block}
  .title__a{color:var(--slate);font-size:29px}
  .title__b{color:var(--forest);font-size:50px}
  .title__c{color:var(--slate);font-size:56px}
  .group-name{position:absolute;left:200px;top:190px;font-family:"Oswald",sans-serif;font-weight:500;color:var(--slate);font-size:17px;line-height:1.2;text-transform:uppercase}
  .led-by{position:absolute;left:200px;top:238px;font-family:"Oswald",sans-serif;font-weight:300;color:var(--slate);font-size:11.5px;line-height:1.6}
  .led-by strong{display:block;font-weight:500;font-size:16px;color:#6e7073;margin-top:1px}
  .topics-band{position:absolute;left:155px;top:448px;width:213px;height:23px;background:var(--sage);color:var(--white);
    font-family:"Josefin Sans",sans-serif;font-weight:600;font-size:15px;letter-spacing:3px;padding:5px 0 0 10px}
  .badge{position:absolute;left:30px;width:94px;height:94px;border-radius:50%;border:3px solid var(--paper);color:var(--white);
    font-family:"Varela Round",sans-serif;display:flex;flex-direction:column;align-items:center;justify-content:center;text-align:center;line-height:1.2}
  .badge--weeks{top:463px;background:var(--mist-blue);font-size:16px}
  .badge--cost{top:547px;background:var(--sage);font-size:16px}
  .badge--cost b{font-weight:400;font-size:22px;line-height:1}
  .badge--cost small{font-size:11px}
  .badge--size{top:630px;background:var(--mist-blue);font-size:10.5px}
  .topics{position:absolute;left:162px;top:490px;list-style:none;font-size:12.3px;color:var(--ink)}
  .topics li{display:flex;align-items:center;gap:7px;height:20px}
  .topics svg{width:8px;height:8px;flex:none}
  .contact-lead{position:absolute;left:0;width:368px;top:740px;text-align:center;color:var(--body-grey);font-size:10.5px}
  .contact-lead strong{display:block;font-size:14px;color:#55575a;font-weight:900;margin-top:4px}
  .contact-lead strong span{font-weight:400}
  .contact-band{position:absolute;background:var(--sage);color:var(--white);text-align:center}
  .card--front .contact-band{left:0;top:778px;width:368px;height:51px;padding-top:7px}
  .card--back .contact-band{left:26px;top:765px;width:315px;height:46px;padding-top:6px}
  .contact-band__phone{font-weight:900;font-size:17.5px;display:flex;align-items:center;justify-content:center;gap:3px}
  .contact-band__phone svg{width:12px;height:15px}
  .contact-band__email{font-family:"Josefin Sans",sans-serif;font-size:11.5px;letter-spacing:1.6px;display:flex;align-items:center;justify-content:center;gap:4px;margin-top:2px}
  .contact-band__email svg{width:8px;height:6px}

  /* back */
  .note{position:absolute;left:26px;top:33px;width:315px;height:260px;background:var(--sage);color:var(--white);
    padding:33px 19px 0;font-size:11.4px;line-height:1.31;text-align:justify}
  .note p+p{margin-top:15px}
  .note__pointer{position:absolute;left:176px;top:293px;width:0;height:0;border-left:9px solid transparent;border-right:9px solid transparent;border-top:10px solid var(--sage)}
  .note__mark{position:absolute;left:164px;top:12px;width:40px;height:40px;border-radius:50%;background:#3d7a3a;border:3px solid var(--white)}
  .portrait{position:absolute;left:107px;top:317px;width:154px;height:154px;border-radius:50%;border:3px solid #d4d4d4;
    background:radial-gradient(circle at 50% 55%,#b3a89e 0%,#8d7b6d 55%,#6f6259 100%)}
  .bio-name{position:absolute;left:0;width:368px;top:481px;text-align:center;color:var(--ink);font-size:15px;font-weight:400}
  .bio-roles{position:absolute;left:0;width:368px;top:502px;text-align:center;color:var(--ink);font-size:9.3px;line-height:1.3}
  .bio-rule{position:absolute;left:152px;top:537px;width:64px;height:2px;background:var(--mist-blue)}
  .bio{position:absolute;left:40px;top:553px;width:288px;color:var(--body-grey);font-size:12.6px;line-height:1.25;text-align:justify}
  .bio p+p{margin-top:15px}
  .brand--back{left:118px;top:707px;font-size:13px;line-height:1.15;width:140px}
</style>
</head>
<body>

<section class="card card--front">
  <div class="hero-photo" role="img" aria-label="Woman seen from behind sitting on a bench overlooking a calm sea"></div>
  <div class="brand brand--front"><span class="brand__dot"></span><span>Quiet Harbor Counseling</span></div>
  <h1 class="title"><span class="title__a">Mending the</span><span class="title__b">Weary</span><span class="title__c">Spirit</span></h1>
  <h2 class="group-name">Women's Trauma<br>&amp; Loss Group</h2>
  <p class="led-by">Led by Licensed<br>Professional Counselor,<strong>Jen Dalby Rusk</strong></p>

  <div class="topics-band">TOPICS INCLUDE</div>
  <div class="badge badge--weeks">10 Week<br>Group</div>
  <div class="badge badge--cost">Cost<b>$35</b><small>session</small></div>
  <div class="badge badge--size">Group size<br>limited to<br>10 participants</div>

  <ul class="topics">
    <li><svg viewBox="0 0 10 10"><circle cx="5" cy="5" r="4" fill="none" stroke="#7aa77f"/><path d="M3 5l1.6 1.6L8 2.5" fill="none" stroke="#7aa77f" stroke-width="1.2"/></svg>What is Trauma?</li>
    <li><svg viewBox="0 0 10 10"><circle cx="5" cy="5" r="4" fill="none" stroke="#7aa77f"/><path d="M3 5l1.6 1.6L8 2.5" fill="none" stroke="#7aa77f" stroke-width="1.2"/></svg>How Trauma Affects Us</li>
    <li><svg viewBox="0 0 10 10"><circle cx="5" cy="5" r="4" fill="none" stroke="#7aa77f"/><path d="M3 5l1.6 1.6L8 2.5" fill="none" stroke="#7aa77f" stroke-width="1.2"/></svg>Creating a Feeling of Safety</li>
    <li><svg viewBox="0 0 10 10"><circle cx="5" cy="5" r="4" fill="none" stroke="#7aa77f"/><path d="M3 5l1.6 1.6L8 2.5" fill="none" stroke="#7aa77f" stroke-width="1.2"/></svg>Managing Trauma Triggers</li>
    <li><svg viewBox="0 0 10 10"><circle cx="5" cy="5" r="4" fill="none" stroke="#7aa77f"/><path d="M3 5l1.6 1.6L8 2.5" fill="none" stroke="#7aa77f" stroke-width="1.2"/></svg>Importance of Self Care</li>
    <li><svg viewBox="0 0 10 10"><circle cx="5" cy="5" r="4" fill="none" stroke="#7aa77f"/><path d="M3 5l1.6 1.6L8 2.5" fill="none" stroke="#7aa77f" stroke-width="1.2"/></svg>Healthy vs. Unhealthy Coping</li>
    <li><svg viewBox="0 0 10 10"><circle cx="5" cy="5" r="4" fill="none" stroke="#7aa77f"/><path d="M3 5l1.6 1.6L8 2.5" fill="none" stroke="#7aa77f" stroke-width="1.2"/></svg>Guilt, Shame, and Blame</li>
    <li><svg viewBox="0 0 10 10"><circle cx="5" cy="5" r="4" fill="none" stroke="#7aa77f"/><path d="M3 5l1.6 1.6L8 2.5" fill="none" stroke="#7aa77f" stroke-width="1.2"/></svg>Victim vs. Victimized</li>
    <li><svg viewBox="0 0 10 10"><circle cx="5" cy="5" r="4" fill="none" stroke="#7aa77f"/><path d="M3 5l1.6 1.6L8 2.5" fill="none" stroke="#7aa77f" stroke-width="1.2"/></svg>Grieving through Loss</li>
    <li><svg viewBox="0 0 10 10"><circle cx="5" cy="5" r="4" fill="none" stroke="#7aa77f"/><path d="M3 5l1.6 1.6L8 2.5" fill="none" stroke="#7aa77f" stroke-width="1.2"/></svg>Anger and Forgiveness</li>
    <li><svg viewBox="0 0 10 10"><circle cx="5" cy="5" r="4" fill="none" stroke="#7aa77f"/><path d="M3 5l1.6 1.6L8 2.5" fill="none" stroke="#7aa77f" stroke-width="1.2"/></svg>Imagining a Better Future</li>
  </ul>

  <p class="contact-lead">For More Information, Contact<strong>Jen Dalby Rusk, <span>LPC, LMFT</span></strong></p>

  <div class="contact-band">
    <div class="contact-band__phone"><svg viewBox="0 0 12 16"><path d="M4 1L1.5 2.5C0 4 0 9 3.5 13.5 5.5 15.5 7.5 15.5 8.5 14.5L9.5 12.5 7 10.5 5.5 11.5C4 10 3 7 3.5 5L5.5 4.5Z" fill="#fff"/></svg>(555) 614-3920</div>
    <div class="contact-band__email"><svg viewBox="0 0 8 6"><rect width="8" height="6" fill="#fff"/><path d="M0 0l4 3 4-3" fill="none" stroke="#9ac9aa" stroke-width=".8"/></svg>jen@brightmeadowcare.example</div>
  </div>
</section>

<section class="card card--back">
  <div class="note">
    <p>Life hurts and does not seem fair.&nbsp; So what do you do when you are faced with an event in your life that knocks you off your feet?&nbsp; It seems no one understands what you are feeling and no one knows just what to say.&nbsp; It is tempting to pull away and isolate or put up a mask and pretend everything is OK.</p>
    <p>It is my desire you know that you are not alone!&nbsp; There are others who understand the feelings you are going through and offer a safe place for encouraging support.&nbsp; I want to invite you to embark on a courageous journey of healing where you will not only learn how to "survive" after trauma and loss, but instead, learn that you can once again "thrive"!</p>
  </div>
  <div class="note__pointer"></div>
  <svg class="note__mark" viewBox="0 0 40 40" aria-hidden="true">
    <path d="M11 25a4 4 0 1 0 4-4c0-3 1.5-5 4-6l-1-2c-4 1.5-7 5-7 12Z M21 25a4 4 0 1 0 4-4c0-3 1.5-5 4-6l-1-2c-4 1.5-7 5-7 12Z" fill="#fff" transform="translate(-3 -2)"/>
  </svg>

  <div class="portrait" role="img" aria-label="Portrait of Jen Dalby Rusk seated on a beach at sunset"></div>
  <h3 class="bio-name">Jen Dalby Rusk, LPC, LMFT</h3>
  <p class="bio-roles">Licensed Professional Counselor<br>Licensed Marriage and Family Therapist</p>
  <div class="bio-rule"></div>
  <div class="bio">
    <p>Jen Dalby Rusk is a Licensed Professional Counselor and Licensed Marriage and Family Therapist.&nbsp; She is the owner of Quiet Harbor Counseling Services located in Maple Bend, OK.</p>
    <p>Jen is a trauma survivor herself and understands firsthand the unique challenges that can arise on the journey to healing.</p>
  </div>

  <div class="brand brand--back"><span class="brand__dot"></span><span>Quiet Harbor Counseling</span></div>

  <div class="contact-band">
    <div class="contact-band__phone"><svg viewBox="0 0 12 16"><path d="M4 1L1.5 2.5C0 4 0 9 3.5 13.5 5.5 15.5 7.5 15.5 8.5 14.5L9.5 12.5 7 10.5 5.5 11.5C4 10 3 7 3.5 5L5.5 4.5Z" fill="#fff"/></svg>(555) 614-3920</div>
    <div class="contact-band__email"><svg viewBox="0 0 8 6"><rect width="8" height="6" fill="#fff"/><path d="M0 0l4 3 4-3" fill="none" stroke="#9ac9aa" stroke-width=".8"/></svg>jen@brightmeadowcare.example</div>
  </div>
</section>

</body>
</html>
```